Exclusive Wine Label for Australia

We require a new and exclusive wine label for one of our key clients. We are a family winery based in Western Australia with a premium focus. The wine will mainly be sold online so the label will require visual appeal and and a premium focus to fit a price point between $25-$30.

The label will be a revamp of an existing label of ours called Tallow Ridge (bottle image attached) . The only criteria required is to use the name. It can have a totally new look and theme to it. When investigating concepts, look at what the region, Margaret River is know for. It's all about the coastal environment, natural appeal and the relaxed lifestyle that people enjoy when visiting.

The label should be vibrant, colorful and not too serious.

I've also attached one of our labels Tre Colline. This is to give you the structure and layout of how we want the label (please ignore the graphic design and the use of our brand Velmonte) . It's a single wrap label with the dimensions of 88mm tall x 170mm wide.

Our preference is to not use too many expensive finishes such as foils, but embossing and high builds are fine. Velmonte logo is not required and our winery will only be displayed in text where it shows where the product is made.

Target Market(s)

30-50 yrs. No specific gender, but more towards a feminine look

Requirements
Must have
• - Follow the layout of the Tre Colline Label attached.
- Tallow Ridge as the Brand name on label. No reference to Velmonte required
- Fit the price point of $25-30
Nice to have
• It can have a retro look or it can be minimal and modern. I won't put examples up as we are looking for new concepts. Beach themed is the best approach and open to using people on the label as well. Otherwise you can explore making the text as the feature.
Should not have
• Swirls and Waves are overdone. Looking for something more creative.

```html
<!DOCTYPE html>
<html lang="en">
<head>
<meta charset="utf-8">
<title>Tallow Ridge – Wine Label</title>
<link rel="stylesheet" href="https://fonts.googleapis.com/css2?family=Allura&family=Playfair+Display:wght@700&display=swap">
<style>
  :root {
    --canvas: #ffffff;
    --cream: #f4f1e4;
    --blue-light: #4a82bd;
    --blue-mid: #23306e;
    --blue-deep: #120d58;
    --gold: #e0b43a;
    --gold-dark: #b9891f;
    --ink-light: #f7f4ea;
    --facet-cyan: #1aa6dc;
    --facet-teal: #22b3b0;
    --facet-pastel: #d9d2e6;
    --facet-sand: #efd9a8;
  }
  * { margin: 0; padding: 0; box-sizing: border-box; }
  html, body {
    width: 1200px;
    height: 1200px;
    overflow: hidden;
    background: var(--canvas);
  }
  .canvas {
    position: relative;
    width: 1200px;
    height: 1200px;
  }
  .wine-label {
    position: absolute;
    left: 336px;
    top: 72px;
    width: 528px;
    height: 1056px;
  }
  .brand-script {
    font-family: "Allura", cursive;
    fill: var(--ink-light);
  }
  .price-tag {
    font-family: "Playfair Display", serif;
    font-weight: 700;
    fill: var(--ink-light);
  }
</style>
</head>
<body>
<main class="canvas">
  <svg class="wine-label" viewBox="0 0 330 660" xmlns="http://www.w3.org/2000/svg" aria-label="Tallow Ridge wine label">
    <defs>
      <linearGradient id="label-blue" x1="0" y1="0" x2="1" y2="0">
        <stop offset="0" stop-color="var(--blue-light)"/>
        <stop offset="0.45" stop-color="var(--blue-mid)"/>
        <stop offset="1" stop-color="var(--blue-deep)"/>
      </linearGradient>
      <linearGradient id="facet-fill" x1="0" y1="1" x2="1" y2="0">
        <stop offset="0" stop-color="var(--facet-sand)"/>
        <stop offset="0.3" stop-color="var(--facet-pastel)"/>
        <stop offset="0.6" stop-color="var(--facet-teal)"/>
        <stop offset="1" stop-color="var(--facet-cyan)"/>
      </linearGradient>
      <linearGradient id="gold-line" x1="0" y1="1" x2="1" y2="0">
        <stop offset="0" stop-color="var(--gold-dark)"/>
        <stop offset="0.5" stop-color="var(--gold)"/>
        <stop offset="1" stop-color="var(--gold-dark)"/>
      </linearGradient>
    </defs>

    <!-- cream top band -->
    <path class="top-band" d="M0 20 C 60 4, 120 40, 200 48 C 262 53, 302 30, 330 0 L 330 30 C 300 62, 260 72, 200 66 C 120 60, 60 26, 0 42 Z" fill="var(--cream)"/>

    <!-- main blue panel -->
    <path class="label-panel" d="M0 42 C 60 26, 120 60, 200 66 C 260 72, 300 62, 330 30 L 330 660 L 0 660 Z" fill="url(#label-blue)"/>

    <!-- coloured facet corner -->
    <path class="facet-corner" role="img" aria-label="Colourful angular facets in cyan, teal, lilac and sand tones"
          d="M330 240 C 300 330, 230 520, 0 652 L 0 660 L 330 660 Z" fill="url(#facet-fill)"/>
    <path class="gold-rule" d="M330 240 C 300 330, 230 520, 0 652" fill="none" stroke="url(#gold-line)" stroke-width="5"/>

    <!-- brand name -->
    <text class="brand-script" x="132" y="215" font-size="78" text-anchor="middle">Tallow</text>
    <path class="swash-line" d="M0 338 C 30 330, 60 334, 80 336" fill="none" stroke="var(--ink-light)" stroke-width="2"/>
    <text class="brand-script" x="150" y="345" font-size="78" text-anchor="middle">Ridge</text>

    <!-- price -->
    <text class="price-tag" x="152" y="426" font-size="26" text-anchor="middle" letter-spacing="-1">$25-$30</text>
  </svg>
</main>
</body>
</html>
```